Business Card Design for Vintage Jazz

I am a vintage jazz band leader in New York City. My groups play the music of the 1920s, 1930s and 1940s. My website is morvainhale.com for more info on what I do.

I am looking for a two sided business card design that has the look and feel of a really nice business card from the 1930s. I need to convey with the design that my work has that vintage kind of class and style, but also conveys that we are fun and entertaining.

Most importantly it should make a bold staement. If Walt Pemberly had a card, what would it have looked like? I want a card that I feel confident will make an impact and will let people know that my work is te the top that NYC has to offer in vintage jazz..

Note that I have only decided to avoid the "committed payment" option as I have not used this service before. Assuming that I get quality work I will select a design from those presented.

Target Market(s)

people who want to hire my band for events, media, and new fans of the band

Industry/Entity Type

Performing Art

Contact Information for Business Card

Definitely a matte finish, possibly a sort of old style of paper with that brown tint? definitely a thick card.

Requirements
Must have
• FRONT
• My name: Tobias Merrow
• What I do: Bandleader, Guitarist, Vocalist, Songwriter
• Contact Details: morvainhale.com tobias@morvainhale.com 646-555-0184
• BACK
• My Social Media Links:
• facebook.morvainhale.com
• twitter, instagram, linkedin: morvainhale
• I'm also including a photo image I would like to use. The photo's background is not needed, and to be honest isn't really desireable. Just looking to use the image of me.
Nice to have
• I'm attaching which could be used as is, omitted from the card, or altered maybe with text going around the outside of the circle or in some other way. It may need some clean up to the edges of the lettering as we only use it for the website thumbnail.
• If there's space I'd like to include the text "join our mailing list for a free song download: freesong.morvainhale.com" If not perhaps just "Download a Free Song at: freesong.morvainhale.com - something to this end.
Should not have
• anything cartoony. Don't think retro 90s's vision of the swing era, think actual swing era!
• anything modern. Got to look old school
• Try to avoid dark backgrounds. Since we often play in bars and clubs where it is dar, a d
• avoid script fonts.

```html
<!DOCTYPE html>
<html lang="en">
<head>
<meta charset="utf-8">
<title>Tobias Merrow — Business Card</title>
<link rel="stylesheet" href="https://fonts.googleapis.com/css2?family=Source+Sans+3:wght@400;600;700&display=swap">
<style>
  :root {
    --ink: #000000;
    --paper: #ffffff;
    --backdrop: #e9e7e4;
    --card-shadow: rgba(0, 0, 0, 0.18);
  }
  * { margin: 0; padding: 0; box-sizing: border-box; }
  html, body {
    width: 1200px;
    height: 900px;
    overflow: hidden;
    background: var(--backdrop);
    font-family: "Source Sans 3", "Myriad Pro", Arial, sans-serif;
  }
  .canvas { position: relative; width: 1200px; height: 900px; }

  .card {
    position: absolute;
    background: var(--paper);
    box-shadow: 0 4px 14px var(--card-shadow);
    overflow: hidden;
  }
  .card-front { left: 78px; top: 35px; width: 588px; height: 362px; }
  .card-back  { left: 388px; top: 505px; width: 566px; height: 352px; }

  .card-band { position: absolute; inset: 0; width: 100%; height: 100%; }

  .wordmark {
    position: absolute;
    left: 0; right: 0; top: 72px;
    text-align: center;
    font-size: 34px;
    font-weight: 400;
    letter-spacing: 0.04em;
    color: var(--ink);
  }

  .front-name {
    position: absolute;
    left: 0; right: 0; top: 255px;
    padding-left: 28px;
    text-align: center;
    font-size: 27px;
    font-weight: 600;
    color: var(--paper);
  }
  .contact-line {
    position: absolute;
    left: 32px; top: 303px;
    display: flex;
    align-items: center;
    gap: 6px;
    font-size: 15.5px;
    color: var(--paper);
    white-space: nowrap;
  }
  .contact-item { display: inline-flex; align-items: center; gap: 5px; margin-right: 4px; }
  .contact-icon { width: 13px; height: 13px; fill: var(--paper); }

  .back-name {
    position: absolute;
    left: 0; right: 0; top: 66px;
    text-align: center;
    font-size: 41px;
    font-weight: 700;
    color: var(--ink);
  }
  .social-grid {
    position: absolute;
    top: 238px; left: 0; right: 0;
    display: grid;
    grid-template-columns: 252px 1fr;
    column-gap: 34px;
    row-gap: 6px;
    font-size: 15.5px;
    color: var(--paper);
  }
  .social-item { display: flex; align-items: center; gap: 7px; white-space: nowrap; }
  .social-item.left { justify-content: flex-end; }
  .social-mark { width: 13px; height: 13px; background: var(--paper); flex: none; }
  .roles {
    position: absolute;
    left: 0; right: 0; top: 301px;
    text-align: center;
    font-size: 15.5px;
    font-weight: 600;
    letter-spacing: 0.01em;
    text-transform: uppercase;
    color: var(--paper);
  }
</style>
</head>
<body>
<main class="canvas">

  <section class="card card-front" aria-label="Card front">
    <svg class="card-band" viewBox="0 0 588 362" aria-hidden="true">
      <rect x="0" y="198" width="588" height="164" fill="var(--ink)"/>
      <polygon points="414,190 588,190 588,200 404,200" fill="var(--ink)"/>
      <polyline points="0,225 382,225 414,191" fill="none" stroke="var(--paper)" stroke-width="2.5"/>
    </svg>
    <div class="wordmark">Tobias Merrow</div>
    <h1 class="front-name">Tobias Merrow</h1>
    <p class="contact-line">
      <span class="contact-item">
        <svg class="contact-icon" viewBox="0 0 24 24"><path d="M6.6 10.8a15.1 15.1 0 0 0 6.6 6.6l2.2-2.2a1 1 0 0 1 1-.25 11.4 11.4 0 0 0 3.6.57 1 1 0 0 1 1 1V20a1 1 0 0 1-1 1A17 17 0 0 1 3 4a1 1 0 0 1 1-1h3.5a1 1 0 0 1 1 1c0 1.25.2 2.45.57 3.57a1 1 0 0 1-.25 1z"/></svg>
        646-555-0184
      </span>
      <span class="contact-item">
        <svg class="contact-icon" viewBox="0 0 24 24"><path d="M2 5h20v14H2z M3.5 6.5 12 13l8.5-6.5" fill="var(--paper)"/><path d="M3.5 7 12 13.3 20.5 7" fill="none" stroke="var(--ink)" stroke-width="1.6"/></svg>
        tobias@morvainhale.com
      </span>
      <span class="contact-item">
        <svg class="contact-icon" viewBox="0 0 24 24"><circle cx="12" cy="12" r="10"/><path d="M2 12h20M12 2c3 3 3 17 0 20M12 2c-3 3-3 17 0 20" fill="none" stroke="var(--ink)" stroke-width="1.5"/></svg>
        morvainhale.com
      </span>
    </p>
  </section>

  <section class="card card-back" aria-label="Card back">
    <svg class="card-band" viewBox="0 0 566 352" aria-hidden="true">
      <rect x="0" y="190" width="566" height="162" fill="var(--ink)"/>
      <polygon points="420,182 566,182 566,192 410,192" fill="var(--ink)"/>
      <polyline points="0,216 390,216 420,183" fill="none" stroke="var(--paper)" stroke-width="2.5"/>
    </svg>
    <h2 class="back-name">Tobias Merrow</h2>
    <div class="social-grid">
      <span class="social-item left">morvainhale.com <span class="social-mark"></span></span>
      <span class="social-item"><span class="social-mark"></span> morvainhale</span>
      <span class="social-item left">morvainhale <span class="social-mark"></span></span>
      <span class="social-item"><span class="social-mark"></span> morvainhale</span>
    </div>
    <p class="roles">Bandleader, Guitarist, Vocalist, Songwriter</p>
  </section>

</main>
</body>
</html>
```